Hexagon Honey Bottle Design, simple and elegant.

Bottle description:
BODY HEIGHT With cap 8.75cm
Without cap 8.6cm
DIAMETER Inner 4.4cm
Outer 5.2cm
Label height only has to be = 6cm height x (3.4X6) length of one hexagonal box is 3.4cm
See through bottle with black cap.
Concept of design:
Elegant, Simple, no pictures of bees, pictures of honeycomb, wooden honey stick, or drooling honey from either is ok. Simple colors. (Designer's discretion)
Wordings:
Hex1
Product of Yemen
Header:
KORVAL /MELO/ (Brand name)
Explanatory below header
Yemen Sidr Honey from The Valley Ra'ufil (100% Pure)
(name of honey)
250g
Optional
Hex2
Pure
=
No Additives (not even natural additives)
Hex3
Raw
=
Unheated, Unpasteurized, Unprocessed honey
Hex4
Natural
=
No added color, artificial flavor, or synthetic substance
Hex5
RENOWNED
=
Very well known by honey lovers
(Natural Pure Raw and Renowned) wordings to be on a suitable place on the bottle (maybe on the cap) -
Hex6
Imported By
The Lantern Bazaar Pte Ltd
No. 317, Cobalt Ferry Road, #09-12
Cobalt Ferry Plaza
Singapore 195340
Wordings can be rearranged - its up to the designer's discretion where and how to place them and in which order.-
Designer must be willing to do numerous changes as the design develops

```html
<!DOCTYPE html>
<html lang="en">
<head>
<meta charset="utf-8">
<title>Korval Melo – Hexagon Jar Label Set</title>
<link href="https://fonts.googleapis.com/css2?family=Roboto:wght@300;400;500&display=swap" rel="stylesheet">
<style>
  :root {
    --page: #ffffff;
    --honey: #fdb813;
    --honey-pale: #fde2a0;
    --honey-deep: #f29e0c;
    --emblem-bright: #fcd21c;
    --ink-dark: #3a2606;
    --ink: #6b4510;
    --ink-soft: #a0650a;
  }
  * { box-sizing: border-box; margin: 0; padding: 0; }
  html, body {
    width: 1200px; height: 1200px; overflow: hidden;
    background: var(--page);
    font-family: "Roboto", Arial, sans-serif;
  }
  .label-strip {
    position: absolute;
    left: 37px; top: 768px;
    display: flex; gap: 13px;
  }
  .label {
    position: relative;
    width: 180px; height: 318px;
    background: var(--honey);
    border-radius: 0 0 7px 7px;
    overflow: hidden;
    text-align: center;
  }
  .label__drip-edge {
    position: absolute; left: 0; top: 0;
    width: 100%; height: 62px;
    background: linear-gradient(180deg, var(--page) 0, var(--page) 10px, var(--honey-pale) 34px, var(--honey) 62px);
  }
  .label__heading {
    position: absolute; left: 0; right: 0; top: 73px;
    font-weight: 300; font-size: 26px; line-height: 30px;
    color: var(--ink);
  }
  .label__brand {
    position: absolute; left: 0; right: 0; top: 75px;
    font-weight: 500; font-size: 24px; line-height: 30px;
    color: var(--ink-dark); letter-spacing: 0.5px;
  }
  .label__emblem {
    position: absolute; left: 62px; top: 152px;
    width: 56px; height: 70px;
    border-radius: 50% 50% 46% 46%;
    background: var(--honey-deep);
  }
  .label--brand .label__emblem {
    left: 62px; top: 148px; width: 58px; height: 72px;
    background: var(--emblem-bright);
  }
  .label__note {
    position: absolute; left: 6px; right: 6px; top: 252px;
    font-weight: 300; font-size: 9.5px; line-height: 12px;
    color: var(--ink-soft);
  }
  .label__origin {
    position: absolute; left: 6px; right: 6px; top: 234px;
    font-weight: 300; font-size: 9px; line-height: 11px;
    color: var(--ink-soft);
  }
  .label__origin .gap { display: block; height: 5px; }
  .label__honey-name {
    display: block; margin-top: 8px;
    font-weight: 500; font-size: 9.5px; color: var(--ink-dark);
  }
  .label__weight { display: block; margin-top: 8px; }
  .label__importer {
    position: absolute; left: 4px; right: 4px; top: 226px;
    font-weight: 300; font-size: 8.8px; line-height: 13px;
    color: var(--ink-soft);
  }
</style>
</head>
<body>
  <main class="label-strip">
    <section class="label label--brand">
      <div class="label__drip-edge" role="img" aria-label="Dripping honey edge"></div>
      <h1 class="label__brand">KORVAL<br>MELO</h1>
      <div class="label__emblem" role="img" aria-label="Brand bee emblem"></div>
      <p class="label__origin">Yemen Sidr Honey from The<span class="gap"></span>Valley Ra'ufil<br>(100% Pure)
        <span class="label__honey-name">Name of Honey</span>
        <span class="label__weight">250g</span>
      </p>
    </section>

    <section class="label">
      <div class="label__drip-edge" role="img" aria-label="Dripping honey edge"></div>
      <h2 class="label__heading">Pure</h2>
      <div class="label__emblem" role="img" aria-label="Bee emblem"></div>
      <p class="label__note">No Additives<br>(not even natural additives)</p>
    </section>

    <section class="label">
      <div class="label__drip-edge" role="img" aria-label="Dripping honey edge"></div>
      <h2 class="label__heading">Raw</h2>
      <div class="label__emblem" role="img" aria-label="Bee emblem"></div>
      <p class="label__note">Unheated, Unpasteurized,<br>Unprocessed honey</p>
    </section>

    <section class="label">
      <div class="label__drip-edge" role="img" aria-label="Dripping honey edge"></div>
      <h2 class="label__heading">Natural</h2>
      <div class="label__emblem" role="img" aria-label="Bee emblem"></div>
      <p class="label__note">No added color, artificial flavor<br>synthetic substance</p>
    </section>

    <section class="label">
      <div class="label__drip-edge" role="img" aria-label="Dripping honey edge"></div>
      <h2 class="label__heading">Renowned</h2>
      <div class="label__emblem" role="img" aria-label="Bee emblem"></div>
      <p class="label__note">Very well known by honey lovers</p>
    </section>

    <section class="label">
      <div class="label__drip-edge" role="img" aria-label="Dripping honey edge"></div>
      <p class="label__importer">Imported By<br>The Lantern Bazaar Pte Ltd<br>No. 317, Cobalt Ferry Road, #09-12<br>Cobalt Ferry Plaza<br>Singapore 195340</p>
    </section>
  </main>
</body>
</html>
```